4 x Florist Footpath Signage Boards that are consistant with each other for a modern florist

Eye catching, easy to read. little bit floral.
See example attached for wording. We are a modern florist in a country town.
This will be out on the street and needs to stand out!!

The Signage Panels
1. Valentines Day - 14th Feb
2. Workshop Signage boards - see attached example
3. Mothers Day Signage Board - 'Treat mum this Mothers Day'
4. We Are Open

Attached is a copy of the design guidelines and the template. the base of the sign is white.

Target Market(s)

Modern

Industry/Entity Type

Florist

Font styles to use
Sans Serif

Colors
eea4c8
f59296
ffffff
757575

Requirements
Must have
• flowers
• weddings
• giftware
• workshops
• flowers make people happy
• odettemarshpetals.co.nz
Nice to have
• Logo
• little bit of floral or greenery
• my shop is modem and industrial
Should not have
• Needs to be able to read easy

```html
<!DOCTYPE html>
<html lang="en">
<head>
<meta charset="utf-8">
<title>Odette Marsh Petals – We Are Open footpath board</title>
<link rel="stylesheet" href="https://fonts.googleapis.com/css2?family=Barlow+Semi+Condensed:wght@500&display=swap">
<style>
  :root {
    --sign-grey: #737373;
    --sign-pink: #f59296;
    --sign-blush: #eea4c8;
    --sign-white: #ffffff;
    --photo-top: #e8c6cd;
    --photo-mid: #d9a9b4;
    --photo-green: #6f7d5c;
    --photo-deep: #3f4637;
  }
  html, body {
    margin: 0;
    padding: 0;
    width: 907px;
    height: 1200px;
    overflow: hidden;
    background: var(--sign-white);
  }
  .board {
    display: block;
    width: 907px;
    height: 1200px;
  }
  .board-text {
    font-family: "Barlow Semi Condensed", "Arial Narrow", sans-serif;
    font-weight: 500;
    fill: var(--sign-grey);
  }
  .accent-bar { fill: var(--sign-pink); }
  .info-panel { fill: var(--sign-white); }
  .hang-slot { fill: var(--sign-white); stroke: #444; stroke-width: 1; }
  .board-outline { fill: none; stroke: #555; stroke-width: 1; }
  .brand-mark { fill: var(--sign-pink); }
</style>
</head>
<body>
<svg class="board" viewBox="0 0 907 1200" xmlns="http://www.w3.org/2000/svg">
  <defs>
    <linearGradient id="floral-photo-tones" x1="0" y1="0" x2="0.35" y2="1">
      <stop offset="0" stop-color="var(--photo-top)"/>
      <stop offset="0.45" stop-color="var(--photo-mid)"/>
      <stop offset="0.75" stop-color="var(--photo-green)"/>
      <stop offset="1" stop-color="var(--photo-deep)"/>
    </linearGradient>
  </defs>

  <!-- board silhouette with floral photo backdrop -->
  <g role="img" aria-label="Photograph of pink roses, blossom buds and green foliage filling the sign board">
    <path class="board-photo" fill="url(#floral-photo-tones)"
      d="M46 14 H861 A32 32 0 0 1 893 46 V1096 A32 32 0 0 1 861 1128 H848 V1186 H58 V1128 H46 A32 32 0 0 1 14 1096 V46 A32 32 0 0 1 46 14 Z"/>
  </g>
  <path class="board-outline"
    d="M46 14 H861 A32 32 0 0 1 893 46 V1096 A32 32 0 0 1 861 1128 H848 V1186 H58 V1128 H46 A32 32 0 0 1 14 1096 V46 A32 32 0 0 1 46 14 Z"/>

  <rect class="hang-slot" x="385" y="58" width="138" height="37" rx="18.5"/>

  <!-- white information panel -->
  <rect class="info-panel" x="86" y="118" width="735" height="962"/>

  <!-- services header -->
  <text class="board-text" x="140" y="198" font-size="68" textLength="224" lengthAdjust="spacingAndGlyphs">FLOWERS</text>
  <text class="board-text" x="768" y="198" font-size="68" text-anchor="end" textLength="254" lengthAdjust="spacingAndGlyphs">WEDDINGS</text>
  <rect class="accent-bar" x="133" y="208" width="641" height="17"/>

  <text class="board-text" x="144" y="364" font-size="130" textLength="622" lengthAdjust="spacingAndGlyphs">WE ARE OPEN</text>

  <rect class="accent-bar" x="133" y="406" width="641" height="16"/>
  <text class="board-text" x="142" y="480" font-size="68" textLength="243" lengthAdjust="spacingAndGlyphs">GIFTWARE</text>
  <text class="board-text" x="766" y="480" font-size="68" text-anchor="end" textLength="304" lengthAdjust="spacingAndGlyphs">WORKSHOPS</text>

  <!-- shop name -->
  <g class="brand-name">
    <rect class="brand-mark" x="443" y="566" width="22" height="22"/>
    <text class="board-text" x="454" y="636" font-size="24" text-anchor="middle" letter-spacing="4">ODETTE MARSH PETALS</text>
  </g>

  <!-- tagline -->
  <text class="board-text" x="242" y="862" font-size="126" textLength="424" lengthAdjust="spacingAndGlyphs">FLOWERS</text>
  <rect class="accent-bar" x="232" y="875" width="446" height="16"/>
  <text class="board-text" x="242" y="946" font-size="60" textLength="420" lengthAdjust="spacingAndGlyphs">MAKE PEOPLE HAPPY</text>

  <text class="board-text" x="240" y="1010" font-size="44" textLength="418" lengthAdjust="spacingAndGlyphs">odettemarshpetals.co.nz</text>
</svg>
</body>
</html>
```